Book Cover Design "WHEN PATIENT MONEY MEETS A CAREFULLY TIMED PLAN"

I need somebody to design a book cover for my book

The title is ...
"WHEN PATIENT MONEY MEETS A CAREFULLY TIMED PLAN"

The sub title is ...
"A simple step-by-step guide to buying the best shares at the best time written specifically for non-professional investors."

The book is 5 inches by 8 inches and we are looking for a cover design. However we will need a high resolution design so we can create large posters and banners etc, We also need the cover to stand out when viewed on Parcelora etc.

The back of the book must have in large writing...
"A book about the stock market for people who don't read books about the stock market."
The back of the book must have in smaller writing...
"An easy to follow, easy to read book, outlining a 15 step process to help you make better investing decisions."

Please don't use a lot or red. The color red signifies losses in the stock market. Please use blue as the dominant color.

Our website is not live yet, but please visit http://brookvalesaverinstitute.plinkdev.uk/ if you want an idea of how its going to look when it goes live. We would be receptive if you design the cover and back cover in the same brand image as the website.

However, please feel free to design what you like, we are open to anything.

Anybody who invests in stocks and shares as a hobby or in any none-professional capacity.

Finance

85cae6
85acd3
0255a3
3277b5
85abd2
cfdeed
cee9f5
33a6d7
0292cd

• A front and back cover!
• A copy of our company logo on the front and back.
• The price of the book on the back (The price is £15.99)
• The ISBN Bar code for 978-1000472913
• Authors name "Desmond Pelham" on the front
• If you could have "Published by the Brookvale Saver Institute" somewhere on the back in small writing, and also the website if possible?
• www.brookvale-saver-institute.com

```html
<!DOCTYPE html>
<html lang="en">
<head>
<meta charset="utf-8">
<title>When Patient Money Meets a Carefully Timed Plan – Book Cover</title>
<link rel="stylesheet" href="https://fonts.googleapis.com/css2?family=Bebas+Neue&family=Kotta+One&family=Oranienbaum&display=swap">
<style>
  :root {
    --paper: #d2e9f5;
    --navy: #0255a3;
    --cyan: #0292cd;
    --sky: #33a6d7;
    --steel: #3277b5;
    --ink: #4a4a4a;
    --art-light: #85cae6;
    --art-mid: #3277b5;
    --art-ground: #7fb84a;
  }
  * { box-sizing: border-box; margin: 0; padding: 0; }
  html, body { width: 1200px; height: 1000px; overflow: hidden; background: var(--paper); }
  .cover {
    position: relative;
    width: 1200px;
    height: 1000px;
    background: var(--paper);
    font-family: "Kotta One", "Oranienbaum", serif;
    overflow: hidden;
  }
  .abs { position: absolute; }

  /* Back cover */
  .back-headline {
    left: 30px; top: 52px; width: 548px;
    text-align: right;
    color: var(--navy);
    font-size: 31px;
    line-height: 49px;
    font-variant: small-caps;
    letter-spacing: 0.5px;
  }
  .back-headline .drop { font-size: 40px; }
  .back-blurb {
    left: 60px; top: 232px; width: 518px;
    text-align: right;
    color: var(--sky);
    font-size: 22px;
    line-height: 32px;
  }
  .back-publisher {
    left: 26px; top: 388px;
    color: var(--sky);
    font-size: 15px;
    line-height: 26px;
  }
  .back-publisher .indent { padding-left: 32px; display: block; }
  .back-url {
    left: 18px; top: 966px;
    color: var(--navy);
    font-size: 13px;
  }

  /* Publisher name mark */
  .imprint {
    display: flex; align-items: center; gap: 8px;
    color: var(--ink);
    font-size: 17px;
    white-space: nowrap;
  }
  .imprint .mark { width: 12px; height: 12px; background: var(--navy); }
  .imprint-back { left: 205px; top: 893px; }
  .imprint-front { left: 815px; top: 893px; }

  /* Spine */
  .spine-title {
    left: 584px; top: 26px;
    writing-mode: vertical-rl;
    font-family: "Bebas Neue", sans-serif;
    font-size: 37px;
    color: var(--cyan);
    white-space: nowrap;
    letter-spacing: 0.3px;
  }
  .spine-author {
    left: 610px; top: 778px;
    writing-mode: vertical-rl;
    color: var(--steel);
    font-size: 20px;
    white-space: nowrap;
  }
  .spine-price {
    left: 566px; top: 722px;
    writing-mode: vertical-rl;
    color: var(--steel);
    font-size: 16px;
    white-space: nowrap;
    word-spacing: 4px;
  }

  /* Front cover */
  .front-title {
    left: 650px; top: 40px; width: 560px;
    text-align: center;
    font-family: "Bebas Neue", sans-serif;
    font-size: 72px;
    line-height: 64px;
    color: var(--cyan);
  }
  .front-author {
    right: 26px; top: 272px;
    color: var(--steel);
    font-size: 23px;
  }
  .front-art {
    left: 700px; top: 318px; width: 415px; height: 348px;
  }
  .front-subtitle {
    left: 650px; top: 676px; width: 545px;
    text-align: center;
    color: var(--steel);
    font-size: 23px;
    line-height: 34px;
  }
</style>
</head>
<body>
<main class="cover">

  <!-- Back cover -->
  <h2 class="abs back-headline"><span class="drop">A</span> book about the stock market<br>for people who don't read books<br>about the stock market</h2>
  <p class="abs back-blurb">An easy to follow, easy to read book, outlining a 15 step process to help you make better investing decisions</p>
  <p class="abs back-publisher">Published by the<span class="indent">Brookvale Saver Institute</span></p>
  <div class="abs imprint imprint-back"><span class="mark"></span>Brookvale Saver Institute</div>
  <p class="abs back-url">www.brookvale-saver-institute.com</p>

  <!-- Spine -->
  <div class="abs spine-title">WHEN PATIENT MONEY MEETS A CAREFULLY TIMED PLAN</div>
  <div class="abs spine-author">Desmond Pelham</div>
  <div class="abs spine-price">£15.99 ISBN 978-1000472913</div>

  <!-- Front cover -->
  <h1 class="abs front-title">WHEN PATIENT MONEY<br>MEETS A CAREFULLY<br>TIMED PLAN</h1>
  <p class="abs front-author">Desmond Pelham</p>
  <svg class="abs front-art" viewBox="0 0 415 348" role="img" aria-label="Illustration of an investor with a briefcase reaching up to drop a coin into a large blue signpost-shaped money box on a patch of grass">
    <defs>
      <linearGradient id="artTone" x1="0" y1="0" x2="0" y2="1">
        <stop offset="0" stop-color="var(--art-light)"/>
        <stop offset="0.8" stop-color="var(--art-mid)"/>
        <stop offset="1" stop-color="var(--art-ground)"/>
      </linearGradient>
    </defs>
    <rect width="415" height="348" rx="6" fill="url(#artTone)" opacity="0.55"/>
  </svg>
  <p class="abs front-subtitle">A simple step-by-step guide to buying the best shares at the best time written specifically for retail investors</p>
  <div class="abs imprint imprint-front"><span class="mark"></span>Brookvale Saver Institute</div>

</main>
</body>
</html>
```